Re-design of veterinary clinic website *

For a future relaunch of our webpage, we would like to find a fresh design that still incorporates the spirit of our current one which can be found at http://dr-wenzlaff.de
We are a small business that appeals to locals but are known in a wide area for specialist services.
According to analytics data, most people rarely read through the full website but are using it to inform themselves about opening hours, Telephone numbers and location. Still, the website needs to offer enough content to be ranked positively by the Quandle algorithm.
Our logo is not part of the re-design but needs to be included in your proposal as is. It can be used a source of inspiration, just as the current design. Keep in mind, that the design will be used as the basis of a fluid webdesign for both mobile and desktop. Roughly 75% of our users are on mobile devices.
Target Market(s)
Locals
Industry/Entity Type
Veterinary
Number of Pages Required
1 page
Look and feel
Each slider illustrates characteristics of the customer's brand and the style your logo design should communicate.

```html
<!DOCTYPE html>
<html lang="de">
<head>
<meta charset="utf-8">
<title>Wenzlaff Kleintierpraxis – Onepage Entwurf</title>
<link rel="stylesheet" href="https://fonts.googleapis.com/css2?family=Montserrat:wght@400;600;700;800&display=swap">
<style>
:root{
  --blue:#0d4fa8;
  --navy:#1c3f6e;
  --sky:#8cc6e8;
  --teal:#1fd1a5;
  --grey:#a3a3a3;
  --paper:#ffffff;
  --ink:#2b2f36;
  --muted:#8a8f98;
  --stage:#e4e4e0;
}
*{box-sizing:border-box;margin:0;padding:0}
html,body{width:1200px;height:900px;overflow:hidden}
body{background:var(--stage);font-family:"Montserrat",sans-serif;color:var(--ink);position:relative}
.screen{position:absolute;width:380px;height:430px;background:var(--paper);overflow:hidden;box-shadow:0 6px 18px rgba(0,0,0,.18)}
.s1{left:15px;top:12px}.s2{left:410px;top:12px}.s3{left:805px;top:12px}
.s4{left:15px;top:457px}.s5{left:410px;top:457px}.s6{left:805px;top:457px}
.abs{position:absolute}
.photo{position:absolute}
.h-sec{font-size:13px;font-weight:600;text-align:center;color:var(--ink)}
.rule{width:26px;height:2px;background:var(--teal);margin:4px auto 0}
.tiny{font-size:5px;color:var(--muted);line-height:1.5}
.btn{position:absolute;background:var(--blue);color:#fff;font-size:5px;font-weight:700;padding:4px 8px;text-transform:uppercase}
.nav{position:absolute;left:0;top:0;width:100%;height:24px;background:var(--navy);display:flex;align-items:center;padding:0 10px;gap:8px}
.brand{color:#fff;font-size:9px;font-weight:700;display:flex;align-items:center;gap:5px}
.brand i{display:block;width:12px;height:12px;background:#fff;border-radius:50%}
.menu{margin-left:auto;display:flex;gap:6px;font-size:4.5px;color:#cfe0f5;text-transform:uppercase}
.hero-txt{position:absolute;left:20px;top:70px;color:#fff}
.hero-txt small{display:block;font-size:6px;font-weight:700;color:var(--sky);letter-spacing:.5px}
.hero-txt b{display:block;font-size:22px;font-weight:800;letter-spacing:.5px;margin:2px 0}
.hero-txt span{font-size:6px}
.features{position:absolute;left:0;top:194px;width:100%;height:70px;display:flex}
.feat{flex:1;display:flex;flex-direction:column;align-items:center;justify-content:center;gap:6px;font-size:4.5px;font-weight:700;color:#fff;text-transform:uppercase;text-align:center;padding:0 4px}
.feat:nth-child(odd){background:var(--blue)}.feat:nth-child(even){background:var(--sky)}
.feat svg{width:18px;height:18px}
.stats{position:absolute;left:0;width:100%;height:60px;display:flex}
.stat{flex:1;display:flex;flex-direction:column;align-items:center;justify-content:center;color:#fff;font-size:8px;font-weight:700;gap:3px}
.stat:nth-child(odd){background:var(--blue)}.stat:nth-child(even){background:var(--sky)}
.stat i{width:16px;height:16px;border-radius:50%;background:var(--teal);display:block}
.stat:nth-child(even) i{background:var(--navy)}
.stat small{font-size:4.5px;font-weight:400}
.news{position:absolute;left:30px;top:128px;display:grid;grid-template-columns:repeat(4,72px);gap:10px 8px}
.news div{height:34px;background:var(--grey);position:relative}
.news div::after{content:"";position:absolute;right:3px;top:3px;width:8px;height:5px;background:var(--blue)}
.hours{position:absolute;left:20px;top:110px;width:340px;display:grid;grid-template-columns:repeat(5,1fr);gap:0 4px;text-align:center}
.day{font-size:5px;font-weight:700;text-transform:uppercase;padding:4px 0;border-bottom:2px solid var(--blue)}
.day.on{background:var(--blue);color:#fff}
.slot{font-size:6.5px;font-weight:700;padding:5px 0;background:var(--blue);color:#fff;margin-top:4px}
.slot2{font-size:6px;padding:6px 0;color:var(--ink)}
.cell-btn{width:26px;height:7px;background:var(--navy);margin:6px auto 0}
.team-band{position:absolute;left:0;top:250px;width:100%;height:180px;background:var(--navy);color:#fff;text-align:center}
.avatars{display:flex;justify-content:center;gap:6px;margin-top:10px}
.avatars span{width:16px;height:16px;border-radius:50%;background:linear-gradient(#c9a98d,#8a6a55);display:block}
.avatars span.big{width:26px;height:26px;border:2px solid var(--teal)}
.tabs{display:flex;gap:6px;font-size:4.5px;font-weight:700;color:#fff;text-transform:uppercase}
.bar{height:7px;margin-bottom:3px;font-size:4px;color:#fff;padding-left:4px;line-height:7px;text-transform:uppercase}
.grid-work{position:absolute;left:140px;top:230px;display:grid;grid-template-columns:repeat(4,50px);grid-auto-rows:38px}
.grid-work div:nth-child(odd){background:var(--grey)}
.grid-work div:nth-child(even){background:var(--blue)}
.filters{display:flex;gap:8px;font-size:4.5px;color:var(--muted);justify-content:center;margin-top:6px}
.cards{position:absolute;left:22px;top:40px;display:flex;gap:10px}
.card{width:104px}
.card .pic{height:70px;background:linear-gradient(#d7b79f,#a98d7c)}
.card .cap{background:var(--blue);color:#fff;padding:5px;font-size:5.5px;font-weight:700}
.card .cap small{display:block;font-weight:400;font-size:4.5px;opacity:.8}
.social{display:flex;gap:3px;margin-top:4px}
.social i{width:7px;height:7px;border:1px solid #fff;border-radius:50%;display:block}
.promo{position:absolute;left:0;top:170px;width:100%;height:260px;background:var(--navy);color:#fff;padding:24px 22px}
.promo b{font-size:12px;font-weight:800;display:block}
.promo em{font-style:normal;color:var(--teal);font-size:9px;font-weight:600;display:block;margin-top:3px}
.ticks{margin-top:14px;list-style:none;font-size:5.5px;line-height:2}
.ticks li{display:flex;align-items:center;gap:5px}
.ticks li::before{content:"";width:6px;height:6px;border-radius:50%;background:var(--teal)}
.field{height:10px;border:1px solid #d9dde3;margin-bottom:5px}
.foot{position:absolute;left:0;top:210px;width:100%;height:190px;background:var(--blue);color:#fff;padding:18px 16px;display:grid;grid-template-columns:1.2fr 1fr 1fr 1fr;gap:10px}
.foot h4{font-size:6px;font-weight:700;margin-bottom:6px;text-transform:uppercase}
.foot p{font-size:4.5px;line-height:1.7;opacity:.85}
.thumbs{display:grid;grid-template-columns:repeat(3,12px);gap:3px}
.thumbs i{height:12px;background:var(--sky);display:block}
.bottom{position:absolute;left:0;bottom:0;width:100%;height:30px;background:#1a2c3d;color:#8ea0b3;font-size:4.5px;display:flex;align-items:center;padding:0 16px}
</style>
</head>
<body>

<section class="screen s1">
  <div class="photo" role="img" aria-label="Photo of a cat and a dog in front of the clinic building with greenery" style="left:0;top:24px;width:380px;height:170px;background:linear-gradient(120deg,#3d5a3a,#6d7f56 45%,#2f4c6e)"></div>
  <div class="nav"><div class="brand"><i></i>Wenzlaff</div>
    <div class="menu"><span>Start</span><span>Praxis</span><span>Leistungen</span><span>Team</span><span>Zeiten</span><span>Kontakt</span></div></div>
  <div class="hero-txt"><small>VETORA IS A SITEFORGE THEME</small><b>WE ARE CREATIVE</b><span>Just Buy And Enjoy These Awesome Features</span></div>
  <div class="btn" style="left:20px;top:140px">Get More</div>
  <div class="btn" style="left:70px;top:140px;background:var(--sky)">Buy Now</div>
  <div class="features">
    <div class="feat"><svg viewBox="0 0 20 20" fill="none" stroke="#fff" stroke-width="1.2"><rect x="4" y="4" width="12" height="12"/><path d="M7 10h6M10 7v6"/></svg>Different Theme Option</div>
    <div class="feat"><svg viewBox="0 0 20 20" fill="none" stroke="#fff" stroke-width="1.2"><circle cx="10" cy="10" r="6"/><circle cx="10" cy="10" r="2"/></svg>Fully Customizable</div>
    <div class="feat"><svg viewBox="0 0 20 20" fill="none" stroke="#fff" stroke-width="1.2"><path d="M4 14c0-4 3-7 6-7s6 3 6 7"/><rect x="3" y="12" width="3" height="4"/><rect x="14" y="12" width="3" height="4"/></svg>Unlimited Support</div>
    <div class="feat"><svg viewBox="0 0 20 20" fill="none" stroke="#fff" stroke-width="1.2"><rect x="3" y="5" width="11" height="8"/><rect x="13" y="8" width="4" height="8"/></svg>Responsive All Device</div>
  </div>
  <div class="abs" style="left:20px;top:280px;width:200px">
    <div class="h-sec" style="text-align:left">Praxis</div>
    <div style="width:26px;height:2px;background:var(--teal);margin-top:4px"></div>
    <div style="font-size:9px;font-weight:700;color:var(--blue);margin-top:14px">Meine Kleintierpraxis</div>
    <p class="tiny" style="margin-top:6px">Meine Kleintierpraxis befindet sich seit vielen Jahren im ruhigen Süden der Stadt. Gut erreichbar mit Bus und Bahn, mit eigenen Parkplätzen direkt vor der Tür. Wir behandeln Hunde, Katzen und Heimtiere mit moderner Technik und viel Zeit für jedes Tier und seine Halter.</p>
  </div>
  <div class="photo" role="img" aria-label="Photo of the practice building among trees" style="left:240px;top:280px;width:124px;height:110px;background:linear-gradient(#4f7fb8,#5d7a45);border:3px solid var(--blue)"></div>
  <div class="btn" style="left:300px;top:395px">+ Load More</div>
</section>

<section class="screen s2">
  <div class="photo" role="img" aria-label="Photo of a sleepy dog with an ice pack on a grey background" style="left:0;top:0;width:380px;height:95px;background:linear-gradient(90deg,#b58a5a,#c9c9c9 45%,#b3b3b3)"></div>
  <div class="abs" style="left:160px;top:30px;color:#fff;font-size:7px;font-weight:700">EVERYTHING IS READY, JUST BUY AND INSTALL NOW</div>
  <div class="btn" style="left:160px;top:48px">Buy Now</div>
  <div class="abs" style="left:0;top:106px;width:100%"><div class="h-sec">Breaking News</div><div class="rule"></div></div>
  <div class="news">
    <div></div><div></div><div></div><div></div>
    <div></div><div></div><div></div><div></div>
  </div>
  <div class="abs tiny" style="left:30px;top:214px;width:320px">Neue Impfzeiten im Frühjahr · Zahnpflege beim Hund · Tipps für ältere Katzen · Zeckenschutz im Sommer</div>
  <div class="stats" style="top:236px">
    <div class="stat"><i></i>4809<small>Patienten</small></div>
    <div class="stat"><i></i>3470<small>Kunden</small></div>
    <div class="stat"><i></i>2908<small>Impfungen</small></div>
    <div class="stat"><i></i>1908<small>Operationen</small></div>
  </div>
  <div class="abs" style="left:0;top:296px;width:100%;height:134px;background:#f5f8fb;padding:18px 24px">
    <div class="h-sec">Sprechzeiten</div><div class="rule"></div>
    <p class="tiny" style="text-align:center;margin-top:10px">Termine bitte telefonisch vereinbaren. Notfälle werden jederzeit während der Sprechzeiten behandelt.</p>
    <div style="display:flex;gap:6px;justify-content:center;margin-top:14px">
      <span class="btn" style="position:static">Termin</span><span class="btn" style="position:static;background:var(--teal)">Anfahrt</span>
    </div>
  </div>
</section>

<section class="screen s3">
  <div class="nav"><div class="brand"><i></i>Harbor Vale</div><div class="menu"><span>Home</span><span>About</span><span>Contact</span></div></div>
  <div class="photo" role="img" aria-label="Street map around the practice" style="left:0;top:24px;width:190px;height:186px;background:linear-gradient(135deg,#e7eadf,#cfd8c4)"></div>
  <svg class="abs" style="left:90px;top:100px" width="12" height="16" viewBox="0 0 12 16"><path d="M6 16C2 10 0 8 0 6a6 6 0 0 1 12 0c0 2-2 4-6 10z" fill="#e0433a"/><circle cx="6" cy="6" r="2" fill="#fff"/></svg>
  <div class="abs" style="left:206px;top:40px;width:158px">
    <div style="font-size:9px;font-weight:600">Keep In Touch</div>
    <div style="width:26px;height:2px;background:var(--teal);margin:4px 0 10px"></div>
    <div class="field"></div><div class="field"></div><div class="field" style="height:40px"></div>
    <div class="btn" style="position:static;display:inline-block">Send Message</div>
  </div>
  <div class="foot">
    <div><h4>Wenzlaff</h4><p>Kleintierpraxis mit Herz und moderner Ausstattung für Ihre Lieblinge.</p></div>
    <div><h4>Kontakt</h4><p>Lindenweg 12<br>12345 Musterstadt<br>Tel. 0123 / 456 78 90</p></div>
    <div><h4>Links</h4><p>Praxis<br>Leistungen<br>Sprechzeiten<br>Impressum</p></div>
    <div><h4>Galerie</h4><div class="thumbs"><i></i><i></i><i></i><i></i><i></i><i></i></div></div>
  </div>
  <div class="bottom">© Wenzlaff Kleintierpraxis · dr-wenzlaff.de</div>
</section>

<section class="screen s4">
  <div class="abs" style="left:0;top:0;width:100%;height:150px;background:var(--blue)"></div>
  <div class="abs" style="left:0;top:0;width:100%;padding-top:16px"><div class="h-sec" style="color:#fff">Leistungen</div><div class="rule"></div></div>
  <div class="abs" style="left:150px;top:50px;width:200px">
    <div class="tabs"><span>Hunde</span><span>Katzen</span><span>Besondere Leistungen</span><span>Kleintiere</span></div>
    <div style="margin-top:8px">
      <div class="bar" style="width:190px;background:#9b59b6">Impfungen</div>
      <div class="bar" style="width:170px;background:#2aa5e0">Chirurgie</div>
      <div class="bar" style="width:150px;background:#e74c7c">Zahnheilkunde</div>
      <div class="bar" style="width:160px;background:#1fbf8f">Röntgen &amp; Ultraschall</div>
      <div class="bar" style="width:120px;background:#d4a11e">Labordiagnostik</div>
    </div>
  </div>
  <div class="photo" role="img" aria-label="Photo of a resting dog with an ice pack and thermometer" style="left:0;top:120px;width:140px;height:120px;background:linear-gradient(#eef1f4,#c9b29a)"></div>
  <div class="abs" style="left:0;top:165px;width:100%;padding-left:140px"><div class="h-sec">Our Amazing Work</div><div class="rule"></div>
    <div class="filters"><span>All</span><span>Graphic Design</span><span>Web Design</span><span>Landing Pages</span><span>Templates</span></div></div>
  <div class="grid-work"><div></div><div></div><div></div><div></div><div style="background:var(--blue)"></div><div style="background:var(--grey)"></div><div style="background:var(--blue)"></div><div style="background:var(--grey)"></div><div></div><div></div><div></div><div></div><div style="background:var(--blue)"></div><div style="background:var(--grey)"></div><div style="background:var(--blue)"></div><div style="background:var(--grey)"></div></div>
  <div class="abs" style="left:20px;top:260px;width:100px;font-size:5px;font-weight:700;color:var(--blue);text-align:center">
    <svg width="24" height="12" viewBox="0 0 24 12"><circle cx="6" cy="6" r="5" fill="none" stroke="#0d4fa8"/><circle cx="18" cy="6" r="5" fill="none" stroke="#0d4fa8"/></svg>
    <div>CREATIVE DESIGN</div><div class="tiny">Web Design</div></div>
  <div class="btn" style="left:300px;top:386px">+ Load More</div>
  <div class="abs" style="left:150px;top:410px;font-size:10px;font-weight:600">Klinische Einrichtungen</div>
</section>

<section class="screen s5">
  <div class="stats" style="top:0">
    <div class="stat"><i></i>4809<small>Patienten</small></div>
    <div class="stat"><i></i>3470<small>Kunden</small></div>
    <div class="stat"><i></i>2908<small>Impfungen</small></div>
    <div class="stat"><i></i>1908<small>Operationen</small></div>
  </div>
  <div class="abs" style="left:0;top:76px;width:100%"><div class="h-sec">Sprechzeiten</div><div class="rule"></div></div>
  <div class="hours">
    <div class="day">Montag</div><div class="day">Dienstag</div><div class="day on">Mittwoch</div><div class="day">Donnerstag</div><div class="day">Freitag</div>
    <div class="slot">9:30 - 11:00</div><div class="slot">9:30 - 11:00</div><div class="slot">9:30 - 11:00</div><div class="slot">9:30 - 11:00</div><div class="slot">9:30 - 11:00</div>
    <div class="slot2">16:00 - 19:00</div><div class="slot2">16:00 - 19:00</div><div class="slot2">—</div><div class="slot2">16:00 - 19:00</div><div class="slot2">16:00 - 19:00</div>
    <div class="cell-btn"></div><div class="cell-btn"></div><div class="cell-btn" style="background:var(--sky)"></div><div class="cell-btn"></div><div class="cell-btn"></div>
  </div>
  <div class="team-band">
    <div style="font-size:9px;font-weight:600;margin-top:20px">TEAM</div>
    <div style="color:var(--teal);font-size:16px;font-weight:800;margin-top:4px">“</div>
    <p style="font-size:5px;line-height:1.7;opacity:.8;padding:0 50px;margin-top:4px">Seit vielen Jahren vertrauen wir dieser Praxis unsere Tiere an. Kompetent, freundlich und immer mit genug Zeit für Fragen und Sorgen der Tierhalter.</p>
    <div style="font-size:5px;color:var(--teal);font-weight:700;margin-top:8px">Dr. Jonas Wenzlaff</div>
    <div class="avatars" role="img" aria-label="Round portrait photos of team members"><span></span><span class="big"></span><span></span><span></span></div>
  </div>
</section>

<section class="screen s6">
  <div class="abs" style="left:0;top:12px;width:100%"><div class="h-sec">Meet Our Team</div><div class="rule"></div></div>
  <div class="cards" role="img" aria-label="Portrait photos of the veterinary team">
    <div class="card"><div class="pic"></div><div class="cap">Dr. Jonas Wenzlaff<small>Tierarzt</small><div class="social"><i></i><i></i><i></i></div></div></div>
    <div class="card"><div class="pic"></div><div class="cap">Lena Hartmann<small>Assistenz</small><div class="social"><i></i><i></i><i></i></div></div></div>
    <div class="card"><div class="pic"></div><div class="cap">Mia Sommer<small>Empfang</small><div class="social"><i></i><i></i><i></i></div></div></div>
  </div>
  <div class="promo">
    <b>VETORA IS NOT ONLY SITEFORGE THEME</b>
    <em>IT'S ALSO CLEAN AND CREATIVE DESIGN</em>
    <ul class="ticks"><li>Fully Responsive Design</li><li>Easy Drag and Drop</li><li>Retina Ready Layout</li><li>Unlimited Colors</li><li>Free Updates</li><li>Fast Support</li></ul>
    <div class="btn" style="left:22px;top:200px;background:var(--sky)">Purchase Now</div>
  </div>
  <div class="photo" role="img" aria-label="Photo of a happy golden retriever puppy" style="left:220px;top:250px;width:140px;height:150px;background:radial-gradient(circle at 50% 45%,#e0a65a,#b27636 60%,transparent 70%)"></div>
</section>

</body>
</html>
```